Association Insurance WhitePaper

Need white paper layout design for cover page, data pages and back page, much like a powerpoint design. Looking for similar designs as the uploaded drawing style.

```html
<!DOCTYPE html>
<html lang="en">
<head>
<meta charset="utf-8">
<title>Harlow Association Insurance – White Paper 2025</title>
<link href="https://fonts.googleapis.com/css2?family=Poppins:wght@300;400;500;600;700&family=Oswald:wght@500&display=swap" rel="stylesheet">
<style>
  :root{
    --navy:#0e2f57;
    --navy-deep:#0a2547;
    --blue:#1c6fc4;
    --teal:#14d9a9;
    --ink:#222a33;
    --muted:#59626d;
    --grey-bar:#c9ccd0;
    --grey-dark:#4a4b4d;
    --panel:#eceef0;
    --paper:#ffffff;
  }
  *{box-sizing:border-box;margin:0;padding:0}
  html,body{width:1200px;height:1174px;overflow:hidden;background:#fff}
  body{position:relative;font-family:"Poppins",Arial,sans-serif;color:var(--ink)}
  .page{position:absolute;width:348px;height:492px;background:var(--paper);
    box-shadow:0 2px 8px rgba(0,0,0,.18);overflow:hidden}
  .page--cover{left:48px;top:51px}
  .page--importance{left:426px;top:51px}
  .page--coverage{left:805px;top:51px}
  .page--claims{left:252px;top:587px}
  .page--back{left:655px;top:587px}
  .abs{position:absolute}

  /* artwork placeholders */
  .art{position:absolute;z-index:0}
  .art--sky-blue{left:0;bottom:0;width:100%;height:130px;
    background:linear-gradient(180deg,rgba(255,255,255,0) 0%,#a9c3dd 30%,#4f7fae 65%,#23507f 100%)}
  .art--sky-sunset{left:0;bottom:0;width:100%;height:136px;
    background:linear-gradient(180deg,rgba(255,255,255,0) 0%,#f6c58a 25%,#e57b3c 55%,#a8391f 80%,#36466a 100%)}
  .art--sky-pastel{left:0;bottom:0;width:100%;height:150px;
    background:linear-gradient(90deg,#e9b5c8 0%,#b8d8ec 25%,#f4dc8c 50%,#a7dccd 75%,#c4c8ee 100%);
    -webkit-mask:linear-gradient(180deg,transparent 0%,#000 25%,#000 75%,transparent 100%);
            mask:linear-gradient(180deg,transparent 0%,#000 25%,#000 75%,transparent 100%)}
  .art--sky-green{left:0;bottom:0;width:100%;height:100px;
    background:linear-gradient(90deg,#e9a0a0 0%,#9bd3c5 30%,#7fbfd8 55%,#a6d6a0 80%,#f0c38e 100%);
    -webkit-mask:linear-gradient(180deg,transparent 0%,#000 40%,#000 70%,transparent 100%);
            mask:linear-gradient(180deg,transparent 0%,#000 40%,#000 70%,transparent 100%)}
  .art--park{left:0;bottom:0;width:100%;height:128px;
    background:linear-gradient(180deg,rgba(255,255,255,0) 0%,#b9d3de 22%,#7fbf7a 55%,#3f8f3e 100%)}
  .art--building{border-radius:40%}
  .art--b-blue{background:radial-gradient(ellipse at center,#4f98d6 0%,#a9cdea 50%,rgba(255,255,255,0) 70%)}
  .art--b-green{background:radial-gradient(ellipse at center,#8aa88a 0%,#c8d8c4 50%,rgba(255,255,255,0) 70%)}
  .art--b-warm{background:radial-gradient(ellipse at center,#d98b5f 0%,#ecc8ae 50%,rgba(255,255,255,0) 70%)}
  .art--b-pink{background:radial-gradient(ellipse at center,#e0a0c0 0%,#c5d6ee 50%,rgba(255,255,255,0) 70%)}
  .art--b-forest{background:radial-gradient(ellipse at center,#3f7a45 0%,#a9cca3 50%,rgba(255,255,255,0) 70%)}

  /* shared header band */
  .section-head{position:absolute;background:var(--navy);color:#fff;font-weight:600;
    font-size:10.5px;display:flex;align-items:center;justify-content:center;
    box-shadow:0 3px 3px rgba(0,0,0,.35);z-index:2}

  /* footer brand */
  .footer-brand{position:absolute;left:25px;bottom:16px;display:flex;align-items:center;gap:4px;z-index:2}
  .footer-brand .mark{width:14px;height:14px;background:var(--navy)}
  .footer-brand .name{font-size:5.5px;font-weight:600;color:#fff;line-height:1.1;text-transform:uppercase}
  .social{position:absolute;bottom:16px;right:25px;display:flex;gap:5px;z-index:2}
  .social span{width:12px;height:12px;border-radius:50%;border:1px solid #fff}
  .social--dark span{border-color:var(--navy)}

  /* cover */
  .cover-ribbon{position:absolute;left:237px;top:0;width:93px;height:108px}
  .cover-year{position:absolute;left:237px;top:52px;width:93px;text-align:center;color:#fff;
    font-weight:700;font-size:15px;letter-spacing:.5px}
  .cover-brand{position:absolute;left:25px;top:148px;display:flex;align-items:center;gap:8px}
  .cover-brand .mark{width:44px;height:44px;background:var(--navy)}
  .cover-brand .name{color:var(--ink);font-weight:500;line-height:1.1}
  .cover-brand .name b{display:block;font-size:13.5px;font-weight:500}
  .cover-brand .name small{display:block;font-size:8px;font-weight:500}
  .cover-title{position:absolute;left:25px;top:227px;width:310px;font-size:15.5px;font-weight:700;color:#2a2f36;line-height:1.35}
  .cover-title span{display:block;font-weight:300;font-size:14.5px}
  .cover-band{position:absolute;left:0;top:289px;width:270px;height:21px}
  .cover-band-text{position:absolute;left:25px;top:289px;height:21px;display:flex;align-items:center;
    color:#fff;font-size:7px}

  /* importance page */
  .feature{position:absolute;width:150px;z-index:2}
  .feature h3{color:var(--blue);font-size:7.4px;font-weight:600;margin-bottom:3px;white-space:nowrap}
  .feature p{font-size:4.8px;line-height:1.65;color:#333}

  /* coverage page */
  .bullets{position:absolute;left:25px;top:68px;width:165px;list-style:none;z-index:2}
  .bullets li{position:relative;padding-left:7px;font-size:6px;line-height:1.65;color:#333;margin-bottom:8px}
  .bullets li::before{content:"";position:absolute;left:0;top:3px;width:3px;height:3px;border:1px solid var(--blue);border-radius:50%}
  .stats{position:absolute;left:214px;top:104px;width:116px;height:49px;background:var(--panel);padding:3px 3px}
  .stats-row{display:flex;align-items:center;font-size:6px;height:14.5px;color:#333}
  .stats-row .label{width:44px}
  .stats-row .val{width:30px}
  .stats-row .up{color:var(--teal)}
  .kpi{position:absolute;left:250px;top:182px;width:80px;height:150px;background:#f4f5f6;z-index:2}
  .kpi-item{position:absolute;left:0;width:80px;height:28px}
  .kpi-ring{position:absolute;left:22px;width:26px;height:26px;border-radius:50%;display:flex;align-items:center;justify-content:center;font-size:4.5px;color:#fff}
  .kpi-note{position:absolute;left:52px;font-size:2.8px;line-height:1.3;color:#555}
  .kpi-year{position:absolute;left:8px;top:99px;font-family:"Oswald",sans-serif;font-size:9.5px;color:#222}
  .kpi-bar{position:absolute;left:8px;height:4px}

  /* claims page */
  .step{position:absolute;left:126px;width:110px;z-index:2}
  .step h4{font-size:7.5px;font-weight:600;color:#111;margin-bottom:2px}
  .step p{font-size:4.2px;line-height:1.6;color:#333}

  /* back page */
  .back-brand{position:absolute;left:54px;top:46px;display:flex;align-items:center;gap:14px}
  .back-brand .mark{width:73px;height:73px;background:var(--navy)}
  .back-brand .name{color:#2a2f36;line-height:1.1}
  .back-brand .name b{display:block;font-size:22px;font-weight:600;letter-spacing:.5px}
  .back-brand .name small{display:block;font-size:12.5px;font-weight:400}
  .contact{position:absolute;left:77px;display:flex;gap:8px;align-items:center}
  .contact .icon{width:23px;height:23px;border:1px solid #b9c0c8;display:flex;align-items:center;justify-content:center}
  .contact .label{font-size:7px;color:var(--muted)}
  .contact .value{font-size:9.5px;color:#222}
  .back-social{position:absolute;left:146px;top:299px;display:flex;gap:7px}
  .back-social span{width:24px;height:24px;border-radius:50%;background:var(--navy)}
  .back-ribbon{position:absolute;left:12px;top:345px;width:324px;height:20px;z-index:2}
  .back-ribbon-text{position:absolute;left:0;top:345px;width:348px;height:20px;display:flex;align-items:center;justify-content:center;color:#fff;font-size:6px;z-index:3}
</style>
</head>
<body>

<!-- Cover -->
<section class="page page--cover">
  <svg class="cover-ribbon" viewBox="0 0 93 108"><polygon points="0,0 93,0 93,108 46.5,89 0,108" fill="var(--navy)"/></svg>
  <div class="cover-year">2025</div>
  <div class="cover-brand">
    <div class="mark"></div>
    <div class="name"><b>HARLOW</b><small>ASSOCIATION INSURANCE</small></div>
  </div>
  <h1 class="cover-title">Community Association Insurance:<span>Protecting Condos &amp; Townhouses</span></h1>
  <svg class="cover-band" viewBox="0 0 270 21"><polygon points="0,0 270,0 262,10.5 270,21 0,21" fill="var(--navy)"/></svg>
  <div class="cover-band-text">Risk Management &amp; Coverage Insights for Homeowners Associations</div>
  <div class="art art--sky-blue" role="img" aria-label="Blue watercolour city skyline"></div>
</section>

<!-- Importance -->
<section class="page page--importance">
  <div class="section-head" style="left:37px;top:11px;width:274px;height:29px">Importance of community association insurance</div>

  <div class="art art--building art--b-blue" style="left:214px;top:52px;width:128px;height:72px" role="img" aria-label="Watercolour sketch of a glass office building"></div>
  <div class="feature" style="left:24px;top:60px">
    <h3>Protecting Your Association, Safeguarding Your Homes</h3>
    <p>Kaerspiciatis unde omnis iste natus error sit voluptatem accusantium doloremque laudantium, totam rem aperiam, eaque ipsa quae ab illo inventore veritatis et quasi architecto beatae vitae dicta sunt explicabo. Nemo enim ipsam voluptatem quia voluptas sit aspernatur aut odit aut fugit.</p>
  </div>

  <div class="art art--building art--b-green" style="left:6px;top:122px;width:118px;height:80px" role="img" aria-label="Sketch of a modern building with roof gardens"></div>
  <div class="feature" style="left:140px;top:140px">
    <h3>Tailored Insurance for Condos &amp; Townhomes</h3>
    <p>Kaerspiciatis unde omnis iste natus error sit voluptatem accusantium doloremque laudantium, totam rem aperiam, eaque ipsa quae ab illo inventore veritatis et quasi architecto beatae vitae dicta sunt explicabo. Nemo enim ipsam voluptatem quia voluptas sit aspernatur aut odit aut fugit.</p>
  </div>

  <div class="feature" style="left:24px;top:218px">
    <h3>Smart Protection for Condo &amp; Townhouse Associations</h3>
    <p>Kaerspiciatis unde omnis iste natus error sit voluptatem accusantium doloremque laudantium, totam rem aperiam, eaque ipsa quae ab illo inventore veritatis et quasi architecto beatae vitae dicta sunt explicabo. Nemo enim ipsam voluptatem quia voluptas sit aspernatur aut odit aut fugit.</p>
  </div>
  <div class="art art--building art--b-green" style="left:232px;top:214px;width:108px;height:66px" role="img" aria-label="Sketch of a green apartment block"></div>

  <div class="art art--building art--b-green" style="left:6px;top:284px;width:120px;height:78px" role="img" aria-label="Sketch of a low building among trees"></div>
  <div class="feature" style="left:140px;top:299px">
    <h3>Strengthen Your Community with Reliable Coverage</h3>
    <p>Kaerspiciatis unde omnis iste natus error sit voluptatem accusantium doloremque laudantium, totam rem aperiam, eaque ipsa quae ab illo inventore veritatis et quasi architecto beatae vitae dicta sunt explicabo. Nemo enim ipsam voluptatem quia voluptas sit aspernatur aut odit aut fugit.</p>
  </div>

  <div class="art art--sky-sunset" role="img" aria-label="Watercolour city skyline at sunset"></div>
  <div class="footer-brand"><span class="mark" style="background:#fff"></span><span class="name">Harlow<br>Association Insurance</span></div>
  <div class="social"><span></span><span></span></div>
</section>

<!-- Coverage -->
<section class="page page--coverage">
  <div class="section-head" style="left:25px;top:17px;width:298px;height:29px;font-size:10px">Key Coverage Areas for Condo &amp; Townhouse Associations</div>

  <ul class="bullets">
    <li>Haasetam rem aperiam, eaque ipsa quae ab illo inventore veritatis et quasi architecto beatae</li>
    <li>Kaerspiciatis unde omnis iste natus error sit voluptatem accusantium doloremque laudantium,</li>
    <li>Gaotam rem aperiam, eaque ipsa quae ab illo inventore veritatis et quasi architecto beatae</li>
    <li>Vaequia voluptas sit aspernatur aut odit aut fugit.</li>
    <li>Gaotam rem aperiam, eaque ipsa quae ab illo inventore veritatis et quasi architecto beatae</li>
    <li style="width:120px">Caeam rem aperiam, eaque ipsa quae ab illo inventore veritatis.</li>
  </ul>

  <div class="stats">
    <div class="stats-row"><span class="label">COMPLETED</span><span class="val up">+86.054</span><span class="up">↑</span></div>
    <div class="stats-row"><span class="label">RECURRING</span><span class="val">-6.230</span><span>↓</span></div>
    <div class="stats-row"><span class="label">PENDING</span><span class="val up">+23.432</span><span class="up">↑</span></div>
  </div>

  <svg class="abs" style="left:25px;top:190px" width="205" height="140" viewBox="0 0 205 140" font-family="Oswald, sans-serif">
    <rect x="14" y="112" width="33" height="25" fill="var(--grey-bar)"/>
    <rect x="49.5" y="111" width="32.5" height="26" fill="var(--grey-dark)"/>
    <rect x="85" y="94.6" width="32" height="42.4" fill="var(--grey-bar)"/>
    <rect x="120" y="83" width="33" height="54" fill="var(--grey-bar)"/>
    <rect x="156" y="48" width="32" height="89" fill="var(--teal)"/>
    <line x1="0" y1="137.5" x2="202" y2="137.5" stroke="#222" stroke-width="1"/>
    <path d="M14 86 C80 82 140 60 182 10" fill="none" stroke="var(--navy-deep)" stroke-width="3"/>
    <polygon points="189,0 176,8 186,16" fill="var(--navy-deep)"/>
    <g font-size="8" fill="#444" text-anchor="middle">
      <text x="30.5" y="108">+10.3</text>
      <text x="66" y="107">+12.0</text>
      <text x="101" y="91">+22.6</text>
      <text x="136.5" y="79">+41.9</text>
      <text x="172" y="44" fill="#111">+83.0</text>
    </g>
  </svg>

  <div class="kpi">
    <div class="kpi-item" style="top:4px">
      <div class="kpi-ring" style="background:var(--teal);box-shadow:0 0 0 2px #bdf4e6">+0.83%</div>
      <div class="kpi-note" style="top:9px">First quarter<br>Jan–Mar</div>
    </div>
    <div class="kpi-item" style="top:35px">
      <div class="kpi-ring" style="background:var(--navy-deep);box-shadow:0 0 0 2px #c9ced6">-1.5%</div>
      <div class="kpi-note" style="top:9px">Second quarter<br>Apr–Jun</div>
    </div>
    <div class="kpi-item" style="top:66px">
      <div class="kpi-ring" style="background:#555;box-shadow:0 0 0 2px #d3d3d3">+0.12%</div>
      <div class="kpi-note" style="top:9px">Third quarter<br>Jul–Sep</div>
    </div>
    <div class="kpi-year">THIS YEAR</div>
    <div class="kpi-bar" style="top:116px;width:30px;background:#aaa"></div>
    <div class="kpi-bar" style="top:124px;width:52px;background:repeating-linear-gradient(45deg,var(--teal) 0 2px,#9ff0dc 2px 4px)"></div>
    <div class="kpi-bar" style="top:132px;width:46px;background:#ddd"></div>
    <div class="kpi-bar" style="top:140px;width:18px;background:#9ff0dc"></div>
  </div>

  <div class="art art--sky-pastel" style="bottom:0" role="img" aria-label="Pastel watercolour city skyline"></div>
  <div class="footer-brand"><span class="mark"></span><span class="name" style="color:var(--navy)">Harlow<br>Association Insurance</span></div>
  <div class="social social--dark"><span></span><span></span></div>
</section>

<!-- Claims -->
<section class="page page--claims">
  <div class="section-head" style="left:25px;top:17px;width:299px;height:29px">Common Claims in Condo &amp; Townhouse Associations</div>

  <svg class="abs" style="left:0;top:0;z-index:1" width="348" height="400" viewBox="0 0 348 400">
    <path d="M140 67 H215 A22.5 22.5 0 0 1 215 112 H133 A21.5 21.5 0 0 0 133 155 H215 A21.5 21.5 0 0 1 215 198 H133 A21.5 21.5 0 0 0 133 241 H215 A22.5 22.5 0 0 1 215 286 H133 A27 27 0 0 0 133 340 H215 A22.5 22.5 0 0 1 215 385 H165" fill="none" stroke="var(--navy)" stroke-width="1"/>
    <g fill="#111">
      <circle cx="140" cy="67" r="1"/>
      <circle cx="231" cy="77" r="3"/>
      <circle cx="111.5" cy="133.5" r="3"/>
      <circle cx="236.5" cy="176.5" r="3"/>
      <circle cx="111.5" cy="219.5" r="3"/>
      <circle cx="237.5" cy="263.5" r="3"/>
      <circle cx="106" cy="313" r="3"/>
      <circle cx="235" cy="364" r="3"/>
      <circle cx="165" cy="385" r="1"/>
    </g>
    <g fill="none" stroke="var(--navy)" stroke-width="0.8">
      <polyline points="182,64.5 185,67 182,69.5"/>
      <polyline points="157,109.5 154,112 157,114.5"/>
      <polyline points="182,152.5 185,155 182,157.5"/>
      <polyline points="157,195.5 154,198 157,200.5"/>
      <polyline points="182,238.5 185,241 182,243.5"/>
      <polyline points="157,283.5 154,286 157,288.5"/>
    </g>
  </svg>

  <div class="step" style="top:76px"><h4>Kcaseiicas Cascasecae</h4><p>Kerspiciatis unde omnis iste natus error sit volupt atem accusantium antium.</p></div>
  <div class="step" style="top:119px"><h4>Kcaseiicas Cascasecae</h4><p>Kerspiciatis unde omnis iste natus error sit volupt atem accusantium antium.</p></div>
  <div class="step" style="top:160px"><h4>Kcaseiicas Cascasecae</h4><p>Kerspiciatis unde omnis iste natus error sit volupt atem accusantium antium.</p></div>
  <div class="step" style="top:205px"><h4>Kcaseiicas Cascasecae</h4><p>Kerspiciatis unde omnis iste natus error sit volupt atem accusantium antium.</p></div>
  <div class="step" style="top:249px"><h4>Kcaseiicas Cascasecae</h4><p>Kerspiciatis unde omnis iste natus error sit volupt atem accusantium antium.</p></div>
  <div class="step" style="top:298px"><h4>Kcaseiicas Cascasecae</h4><p>Kerspiciatis unde omnis iste natus error sit volupt atem accusantium antium.</p></div>
  <div class="step" style="top:350px"><h4>Kcaseiicas Cascasecae</h4><p>Kerspiciatis unde omnis iste natus error sit volupt atem accusantium antium.</p></div>

  <div class="art art--building art--b-forest" style="left:250px;top:55px;width:65px;height:55px" role="img" aria-label="Watercolour tower blocks among trees"></div>
  <div class="art art--building art--b-warm" style="left:10px;top:100px;width:90px;height:55px" role="img" aria-label="Watercolour house with red roof and trees"></div>
  <div class="art art--building art--b-pink" style="left:255px;top:155px;width:65px;height:45px" role="img" aria-label="Pastel row of townhouses"></div>
  <div class="art art--building art--b-green" style="left:10px;top:190px;width:90px;height:75px" role="img" aria-label="Sketch of a building overgrown with plants"></div>
  <div class="art art--building art--b-blue" style="left:248px;top:230px;width:97px;height:65px" role="img" aria-label="Watercolour city buildings"></div>
  <div class="art art--building art--b-warm" style="left:10px;top:310px;width:95px;height:65px" role="img" aria-label="Watercolour apartment building"></div>
  <div class="art art--building art--b-warm" style="left:250px;top:335px;width:85px;height:55px" role="img" aria-label="Brick residential block under clouds"></div>

  <div class="art art--sky-green" role="img" aria-label="Watercolour skyline with wind turbines"></div>
  <div class="footer-brand"><span class="mark"></span><span class="name" style="color:var(--navy)">Harlow<br>Association Insurance</span></div>
  <div class="social social--dark"><span></span><span></span></div>
</section>

<!-- Back -->
<section class="page page--back">
  <div class="back-brand">
    <div class="mark"></div>
    <div class="name"><b>HARLOW</b><small>ASSOCIATION INSURANCE</small></div>
  </div>

  <div class="contact" style="top:160px">
    <div class="icon"><svg width="11" height="8" viewBox="0 0 11 8"><rect width="11" height="8" rx="1" fill="var(--blue)"/><polyline points="0.5,0.8 5.5,4.5 10.5,0.8" fill="none" stroke="#fff" stroke-width="1"/></svg></div>
    <div><div class="label">Email</div><div class="value">info@harlowassociationinsurance.com</div></div>
  </div>
  <div class="contact" style="top:200px">
    <div class="icon"><svg width="10" height="10" viewBox="0 0 24 24"><path d="M6.6 10.8a15.1 15.1 0 0 0 6.6 6.6l2.2-2.2a1 1 0 0 1 1-.25 11.4 11.4 0 0 0 3.6.57 1 1 0 0 1 1 1V20a1 1 0 0 1-1 1A17 17 0 0 1 3 4a1 1 0 0 1 1-1h3.5a1 1 0 0 1 1 1c0 1.25.2 2.45.57 3.57a1 1 0 0 1-.25 1z" fill="var(--blue)"/></svg></div>
    <div><div class="label">Phone Number</div><div class="value">555.010.0199</div></div>
  </div>
  <div class="contact" style="top:237px">
    <div class="icon"><svg width="9" height="12" viewBox="0 0 24 32"><path d="M12 0C5.4 0 0 5.4 0 12c0 9 12 20 12 20s12-11 12-20C24 5.4 18.6 0 12 0z" fill="var(--blue)"/><circle cx="12" cy="12" r="4.5" fill="#fff"/></svg></div>
    <div><div class="label">Address</div><div class="value">410 Alder Lane, Springfield, OR 97477</div></div>
  </div>

  <div class="back-social"><span></span><span></span></div>

  <div class="art art--park" role="img" aria-label="Watercolour city skyline above a green park"></div>
  <svg class="back-ribbon" viewBox="0 0 324 20"><polygon points="0,0 324,0 314,10 324,20 0,20 10,10" fill="var(--navy)"/></svg>
  <div class="back-ribbon-text">© 2025 .All rights reserved.</div>
</section>

</body>
</html>
```